KAVLO ZenOS app needs a fun consumer interface design

KAVLO is a file transfer app aimed at consumers to help them get files onto their ZenOS devices. The app is based around each user having a personalised upload web address, and the ability to issue temporary time limited upload codes to friends and colleagues that they can use to send them files. The first version is already live in the widget shelf but we are working on a second, simplified version. You can see the screen shots for this on www.kavlo-example.com and I have attached a quick guide to app flow. The app now looks like a standard templated ZenOS 7 app. We need a design for the app that give it its own look, whilst retaining the standard ZenOS cues. It needs to look good on Palmo and Slabbo. We have a far east techno feel to the app at the moment with our characters, and we want to keep the logo. The website is currently a simple template, there's an ongoing competition to redesign that too - http://jobs.pitchmarket-example.com/job.aspx?id=813964
We have a working app with a reasonable design - we are looking for someone to take that design, add the polish a professional designer can bring, to make it pixel perfect and stand out as an app that has great design as well as great functionality.
We are also looking for something that works well on Palmo and Slabbo. See the attached screenshots of the Slabbo version - we want that version to look beautiful, not the big empty screen it is now.
Updates
Thanks for the designs so far, they look good. Could you draw them up for Slabbo size screens too please. The signup/login page and new code pages I think need the most attention as each page doesn't collect that much information, and so a lot of the screen is currently blank. I think we need some sort of background to set the content into for these pages.
(file 4 and file 6 are Slabbo screenshots)
The old app is installable for free from the Widget Shelf if that helps you get a feel for it on the Slabbo.
Target Market(s)
Consumers, techno savvy
Industry/Entity Type
Store
Font styles to use
Look and feel
Each slider illustrates characteristics of the customer's brand and the style your logo design should communicate.

```html
<!DOCTYPE html>
<html lang="en">
<head>
<meta charset="utf-8">
<title>KAVLO – Upload Codes &amp; Settings</title>
<link rel="stylesheet" href="https://fonts.googleapis.com/css2?family=Roboto:wght@300;400&display=swap">
<style>
:root{
  --canvas:#7fb1ae;
  --caption:#e4efee;
  --bar-top:#52c6f8;
  --bar-bottom:#17a6ee;
  --screen:#f4f8fb;
  --row:#ffffff;
  --row-active:#e2f0fb;
  --divider:#dde5ea;
  --accent:#29aaf0;
  --text:#454c52;
  --text-soft:#8c959c;
  --label:#7b848a;
  --chevron:#b3bcc2;
  --toggle-track:#e9eef1;
  --off:#ee2a2a;
}
*{box-sizing:border-box;margin:0;padding:0}
html,body{width:1200px;height:900px;overflow:hidden}
body{background:var(--canvas);font-family:"Roboto",sans-serif;font-weight:300;position:relative}
.screen{position:absolute;top:98px;width:355px;height:586px;background:var(--screen);overflow:hidden;box-shadow:0 2px 10px rgba(0,0,0,.18)}
.screen--codes{left:162px}
.screen--settings{left:677px}
.app-bar{height:72px;background:linear-gradient(180deg,var(--bar-top),var(--bar-bottom));color:#fff;position:relative}
.status{height:22px;display:flex;justify-content:flex-end;align-items:center;gap:6px;padding-right:6px;font-size:15px;font-weight:400}
.app-title{position:absolute;left:0;right:0;top:31px;text-align:center;font-size:24px;font-weight:300}
.round-btn{position:absolute;top:32px;width:32px;height:32px}
.round-btn--menu{left:7px}
.round-btn--add{right:6px}
.code-row{position:relative;height:68px;border-bottom:1px solid var(--divider);background:var(--row);padding-left:60px}
.code-row--link{background:var(--row-active);height:72px}
.code-row .icon{position:absolute;left:14px;top:50%;transform:translateY(-50%)}
.code-name{font-size:15px;color:var(--text);padding-top:20px;line-height:18px}
.code-row--link .code-name{padding-top:19px}
.code-meta{font-size:11px;color:var(--text-soft);margin-top:3px}
.chevron{position:absolute;right:14px;top:50%;transform:translateY(-50%)}
.section-label{height:32px;padding:15px 0 0 6px;font-size:11px;color:var(--label);font-weight:400;letter-spacing:.3px}
.setting-row{position:relative;height:45px;background:var(--row);border-bottom:1px solid var(--divider);padding-left:60px;font-size:15px;color:var(--text-soft);line-height:45px}
.setting-row .icon{position:absolute;left:13px;top:50%;transform:translateY(-50%)}
.toggle{position:absolute;right:14px;top:10px;width:44px;height:25px;border-radius:13px;background:var(--toggle-track)}
.toggle .knob{position:absolute;top:0;width:25px;height:25px;border-radius:50%}
.toggle--on .knob{right:0;background:var(--accent)}
.toggle--off .knob{left:0;background:var(--off)}
.caption{position:absolute;top:843px;width:355px;text-align:center;font-size:30px;color:var(--caption);font-weight:300}
.caption--codes{left:162px}
.caption--settings{left:677px}
</style>
</head>
<body>

<svg width="0" height="0" style="position:absolute">
  <defs>
    <symbol id="chev" viewBox="0 0 10 18"><path d="M1 1l8 8-8 8" fill="none" stroke="#b3bcc2" stroke-width="1.4"/></symbol>
    <symbol id="timer" viewBox="0 0 28 28"><path d="M14 3a11 11 0 1 1-8.5 4" fill="none" stroke="#29aaf0" stroke-width="2"/><path d="M14 3v4M8 9l6 6" fill="none" stroke="#29aaf0" stroke-width="2" stroke-linecap="round"/></symbol>
    <symbol id="menu" viewBox="0 0 32 32"><circle cx="16" cy="16" r="15" fill="none" stroke="#fff" stroke-width="1.6"/><path d="M11 12h10M11 16h10M11 20h10" stroke="#fff" stroke-width="1.4"/></symbol>
    <symbol id="status" viewBox="0 0 44 16"><path d="M1 6a11 11 0 0 1 16 0l-8 9z" fill="#fff"/><path d="M20 15h9V3z" fill="#fff"/><rect x="33" y="1" width="8" height="14" rx="1" fill="#fff"/></symbol>
  </defs>
</svg>

<section class="screen screen--codes">
  <header class="app-bar">
    <div class="status"><svg width="44" height="16"><use href="#status"/></svg><span>12:06</span></div>
    <svg class="round-btn round-btn--menu"><use href="#menu"/></svg>
    <h1 class="app-title">Upload Codes</h1>
    <svg class="round-btn round-btn--add" viewBox="0 0 32 32"><circle cx="16" cy="16" r="15" fill="none" stroke="#fff" stroke-width="1.6"/><path d="M16 9v14M9 16h14" stroke="#fff" stroke-width="1.6"/></svg>
  </header>
  <ul class="code-list" style="list-style:none">
    <li class="code-row code-row--link">
      <svg class="icon" width="28" height="30" viewBox="0 0 28 30"><circle cx="14" cy="4" r="3" fill="none" stroke="#29aaf0" stroke-width="1.6"/><path d="M14 7v21M8 12h12M3 18c1 6 6 10 11 10s10-4 11-10" fill="none" stroke="#29aaf0" stroke-width="1.6"/></svg>
      <div class="code-name">My Upload Link</div>
      <div class="code-meta">https://www.my.kavlo-example.com/test2/upload</div>
      <svg class="chevron" width="10" height="18"><use href="#chev"/></svg>
    </li>
    <li class="code-row">
      <svg class="icon" width="28" height="28"><use href="#timer"/></svg>
      <div class="code-name">07YLUJAX</div>
      <div class="code-meta">Expires: 10 May 2014 @ 12:00AM</div>
      <svg class="chevron" width="10" height="18"><use href="#chev"/></svg>
    </li>
    <li class="code-row">
      <svg class="icon" width="28" height="28"><use href="#timer"/></svg>
      <div class="code-name">28LXTRAS</div>
      <div class="code-meta">Expires: 14 May 2014 @ 05:38PM</div>
      <svg class="chevron" width="10" height="18"><use href="#chev"/></svg>
    </li>
    <li class="code-row">
      <svg class="icon" width="28" height="28"><use href="#timer"/></svg>
      <div class="code-name">04DNMARE</div>
      <div class="code-meta">Expires: 02 Jun 2014 @ 07:28AM</div>
      <svg class="chevron" width="10" height="18"><use href="#chev"/></svg>
    </li>
    <li class="code-row">
      <svg class="icon" width="28" height="28"><use href="#timer"/></svg>
      <div class="code-name">58OPQXUI</div>
      <div class="code-meta">Expires: 04 Jul 2014 @ 01:58PM</div>
      <svg class="chevron" width="10" height="18"><use href="#chev"/></svg>
    </li>
  </ul>
</section>

<section class="screen screen--settings">
  <header class="app-bar">
    <div class="status"><svg width="44" height="16"><use href="#status"/></svg><span>12:06</span></div>
    <svg class="round-btn round-btn--menu"><use href="#menu"/></svg>
    <h1 class="app-title">Settings</h1>
  </header>
  <div class="section-label">PROFILE</div>
  <div class="setting-row">
    <svg class="icon" width="26" height="26" viewBox="0 0 26 26"><circle cx="13" cy="13" r="12" fill="none" stroke="#29aaf0" stroke-width="1.4"/><circle cx="13" cy="10" r="4.5" fill="none" stroke="#29aaf0" stroke-width="1.4"/><path d="M5 21c2-4 5-6 8-6s6 2 8 6" fill="none" stroke="#29aaf0" stroke-width="1.4"/></svg>
    Change Username<svg class="chevron" width="10" height="18"><use href="#chev"/></svg>
  </div>
  <div class="setting-row">
    <svg class="icon" width="26" height="26" viewBox="0 0 26 26"><path d="M8 12V8a5 5 0 0 1 10 0v4" fill="none" stroke="#29aaf0" stroke-width="1.4"/><rect x="4" y="12" width="18" height="13" fill="none" stroke="#29aaf0" stroke-width="1.4"/></svg>
    Change Password<svg class="chevron" width="10" height="18"><use href="#chev"/></svg>
  </div>
  <div class="setting-row">
    <svg class="icon" width="26" height="26" viewBox="0 0 26 26" fill="none" stroke="#29aaf0" stroke-width="1.3"><circle cx="4" cy="4" r="2.6"/><circle cx="13" cy="4" r="2.6"/><circle cx="22" cy="4" r="2.6"/><circle cx="4" cy="13" r="2.6"/><circle cx="13" cy="13" r="2.6"/><circle cx="22" cy="13" r="2.6"/><circle cx="4" cy="22" r="2.6"/><circle cx="13" cy="22" r="2.6"/><circle cx="22" cy="22" r="2.6"/></svg>
    Change Pin<svg class="chevron" width="10" height="18"><use href="#chev"/></svg>
  </div>
  <div class="section-label" style="padding-top:19px;height:35px">NOTIFICATIONS</div>
  <div class="setting-row">
    <svg class="icon" width="28" height="20" viewBox="0 0 28 20"><rect x="1" y="1" width="26" height="18" fill="none" stroke="#29aaf0" stroke-width="1.4"/><path d="M1 1l13 10L27 1M1 19l10-9M27 19l-10-9" fill="none" stroke="#29aaf0" stroke-width="1.4"/></svg>
    Notify me via Email
    <span class="toggle toggle--on"><span class="knob"><svg width="25" height="25" viewBox="0 0 25 25"><path d="M7 13l4 4 7-9" fill="none" stroke="#fff" stroke-width="1.6"/></svg></span></span>
  </div>
  <div class="setting-row">
    <svg class="icon" width="28" height="28" viewBox="0 0 28 28" style="left:13px"><rect x="7" y="1" width="14" height="26" rx="2" fill="none" stroke="#29aaf0" stroke-width="1.4"/><path d="M7 5h14M7 22h14M12 24.5h4" stroke="#29aaf0" stroke-width="1.3"/></svg>
    Notify me via Mobile
    <span class="toggle toggle--off"><span class="knob"><svg width="25" height="25" viewBox="0 0 25 25"><path d="M8 8l9 9M17 8l-9 9" stroke="#fff" stroke-width="1.6"/></svg></span></span>
  </div>
</section>

<p class="caption caption--codes">Upload Codes</p>
<p class="caption caption--settings">Settings</p>

</body>
</html>
```